Flyer-Design für Rücken-Massage, Klangtherapie etc.
Sehr kompetent und schnelle Umsetzung, gute Gestaltung, Farblich in Harmonie. Schnelle Änderungen, bin sehr zufrieden. Danke für die super Arbeit.
Zielgruppe
Rücken-Massage, Klangtherapie, Fußreflex-Massage, Quantenheilung
Aufgabenstellung
Text zu den Rubriken können vom Internet entnommen werden.
https://wohlruhe-tonpraxis.ch/

```html
<!DOCTYPE html>
<html lang="de">
<head>
<meta charset="utf-8">
<title>Wohlruhe-Tonpraxis – Flyer</title>
<link rel="stylesheet" href="https://fonts.googleapis.com/css2?family=Exo+2:wght@300;400;500&family=Roboto:wght@700&display=swap">
<style>
:root{
  --lime:#8fd12b;
  --lime-light:#b7e64f;
  --lime-pale:#d8f59a;
  --green-deep:#5fa81a;
  --white:#ffffff;
  --text-dark:#2d4a0a;
  --backdrop:#ece9e4;
  --photo-skin:#c9a07e;
  --photo-green:#7cab45;
  --photo-brass:#a7793c;
  --photo-rust:#8b4a33;
  --photo-foot:#e8c3a8;
  --photo-face:#cfb6a6;
  --flower:#e65a8a;
}
*{margin:0;padding:0;box-sizing:border-box}
html,body{width:1200px;height:768px;overflow:hidden;background:var(--backdrop)}
body{position:relative;font-family:"Exo 2",sans-serif;color:var(--white)}
.flyer{position:absolute;top:27px;width:489px;height:693px;background:linear-gradient(180deg,var(--lime-light),var(--lime) 40%,var(--lime));overflow:hidden;box-shadow:0 6px 18px rgba(0,0,0,.25)}
.flyer--front{left:103px}
.flyer--back{left:636px}
.frame{position:absolute;border:1.5px solid var(--white);z-index:6;pointer-events:none}
.abs{position:absolute}
.photo{position:absolute}

/* front */
.headline{position:absolute;left:0;width:489px;top:34px;text-align:center;font-weight:400;font-size:31px;line-height:36px;z-index:5}
.photo--massage{left:0;top:100px;width:489px;height:290px;background:linear-gradient(110deg,#3f6a2a 0%,var(--photo-green) 25%,var(--photo-skin) 55%,#e7d3c4 85%,#f4efe9 100%)}
.wave{position:absolute;left:0;z-index:2}
.benefits{position:absolute;left:29px;top:145px;z-index:4}
.benefits h2{font-weight:400;font-size:13.5px;letter-spacing:.2px}
.benefits ul{list-style:none;font-size:9.6px;line-height:12.2px;font-weight:500}
.benefits li{padding-left:10px;text-indent:-10px}
.benefits li::before{content:"– "}
.photo--flower{left:-5px;top:318px;width:168px;height:168px;border-radius:50%;background:radial-gradient(circle at 55% 45%,var(--flower),#c33d6c 35%,#f3f0ee 62%,#e9e6e2);z-index:4}
.booking{position:absolute;left:178px;top:386px;font-size:20px;line-height:25px;font-weight:400;z-index:5}
.booking .phone{font-family:"Roboto",sans-serif;font-weight:700;font-size:20px;margin-top:2px;display:block}
.brandband{position:absolute;left:0;top:469px;width:470px;height:80px;background:var(--white);z-index:5;display:flex;align-items:center;padding-left:42px;gap:14px}
.brandband .mark{width:42px;height:42px;border-radius:50%;background:var(--lime)}
.brandband .name{color:var(--lime);font-weight:400;font-size:25px;line-height:26px}
.practice{position:absolute;left:52px;top:564px;font-size:15.5px;line-height:19.5px;z-index:5}
.practice .label{font-size:15px}
.practice .web{display:block;margin-top:7px;font-size:15px}
.prices{position:absolute;left:304px;top:568px;font-size:14px;line-height:17px;z-index:5}

/* back */
.brandtag{position:absolute;left:172px;top:17px;width:167px;height:31px;background:var(--white);z-index:7;display:flex;align-items:center;gap:6px;padding-left:8px}
.brandtag .mark{width:18px;height:18px;border-radius:50%;background:var(--lime)}
.brandtag .name{color:var(--lime);font-size:11px;line-height:12px;font-weight:400}
.photo--bowls{left:241px;top:0;width:248px;height:239px;background:radial-gradient(ellipse at 40% 55%,var(--photo-brass),#6f4a22 45%,var(--photo-rust) 75%,#5c2f1f)}
.photo--foot{left:241px;top:239px;width:248px;height:215px;background:radial-gradient(ellipse at 45% 45%,var(--photo-foot),#d9b293 40%,#c7d9a0 70%,#9fc46a)}
.photo--face{left:0;top:480px;width:250px;height:213px;background:linear-gradient(160deg,#f2eeea 0%,var(--photo-face) 45%,#6b4a35 80%,#f7f7f7 100%)}
.section{position:absolute;z-index:5}
.section h2{font-weight:400;font-size:14.5px;line-height:16px}
.section p{font-size:10px;line-height:13.9px;text-align:justify;font-weight:400}
.section strong{font-weight:500}
.section--sound{left:34px;top:47px;width:169px}
.section--reflex{left:34px;top:230px;width:169px}
.section--quantum{left:264px;top:472px;width:205px}
.section--quantum p{text-align:left;line-height:13.2px;font-size:9.8px}
.section--quantum ul{list-style:none;font-size:9.8px;line-height:13.2px}
.section--quantum li::before{content:"- "}
</style>
</head>
<body>

<section class="flyer flyer--front">
  <div class="photo photo--massage" role="img" aria-label="Frau liegt entspannt bei einer Rückenmassage im Grünen"></div>
  <svg class="wave" style="top:0" width="489" height="170" viewBox="0 0 489 170" aria-hidden="true">
    <path d="M0 0H489V112C400 128 300 150 190 138C110 130 50 112 0 120Z" fill="#8fd12b"/>
    <path d="M0 120C50 112 110 130 190 138C300 150 400 128 489 112V130C400 150 300 168 190 158C110 150 50 132 0 140Z" fill="#d8f59a" opacity=".85"/>
  </svg>
  <svg class="wave" style="top:350px" width="489" height="343" viewBox="0 0 489 343" aria-hidden="true">
    <path d="M0 40C120 20 260 5 489 30V343H0Z" fill="#b7e64f"/>
    <path d="M0 52C140 32 280 20 489 42V343H0Z" fill="#8fd12b"/>
  </svg>
  <h1 class="headline">Ihre Wohlfühloase für<br>Körper und Geist</h1>
  <div class="benefits">
    <h2>RÜCKEN-MASSAGE:</h2>
    <ul>
      <li>steigert lokale Durchblutung</li>
      <li>entspannt Haut, Bindegewebe<br>und Muskulatur</li>
      <li>löst Verklebungen und Narben</li>
      <li>senkt Blutdruck und Pulsfrequenz</li>
      <li>lindert Schmerzen</li>
      <li>bringt psychische Entspannung</li>
      <li>reduziert Stress</li>
    </ul>
  </div>
  <div class="photo photo--flower" role="img" aria-label="Rosa Lilienblüte auf weißem Handtuch"></div>
  <p class="booking">Buchen Sie jetzt Ihren<br>Wohlfühltermin<span class="phone">076 482 19 53</span></p>
  <div class="brandband">
    <span class="mark"></span>
    <span class="name">Wohlruhe-Tonpraxis<br>Mirjam Hollmannsried</span>
  </div>
  <p class="practice"><span class="label">PRAXIS</span><br>Mirjam Hollmannsried<br>Brunnengasse 9<br>4157 Talwil<span class="web">www.wohlruhe-tonpraxis.ch</span></p>
  <p class="prices">PREISE BEHANDLUNG<br>30 Min.: CHF &nbsp;60,00<br>45 Min.: CHF &nbsp;70,00<br>60 Min.: CHF 100.00</p>
  <div class="frame" style="left:17px;top:16px;width:455px;height:658px"></div>
</section>

<section class="flyer flyer--back">
  <div class="photo photo--bowls" role="img" aria-label="Messing-Klangschalen auf rotem Tuch mit Orchidee"></div>
  <div class="photo photo--foot" role="img" aria-label="Hände massieren eine Fusssohle"></div>
  <div class="photo photo--face" role="img" aria-label="Frau liegt entspannt auf Handtuch, Hand an der Stirn"></div>
  <svg class="wave" style="top:0" width="489" height="693" viewBox="0 0 489 693" aria-hidden="true">
    <path d="M0 0H241C236 120 250 300 290 455C330 470 420 440 489 400V480H0Z" fill="#8fd12b"/>
    <path d="M250 480C330 470 420 440 489 400V693H250Z" fill="#b7e64f"/>
    <path d="M262 482C340 475 425 455 489 420V693H262Z" fill="#8fd12b"/>
  </svg>
  <div class="brandtag"><span class="mark"></span><span class="name">Wohlruhe-Tonpraxis<br>Mirjam Hollmannsried</span></div>
  <div class="section section--sound">
    <h2>KLANGTHERAPIE</h2>
    <p>Klangschalen bewirken, dass sich der Körper entkrampft und die Seele sich öffnen kann, die Behandlung wirkt intensiver und hat eine langanhaltende positive Wirkung auf Körper und Seele. Durch die entspannenden Klänge werden neue Selbstheilungskräfte entwickelt die wiederrum zu neuer Lebensenergie verhilft.</p>
  </div>
  <div class="section section--reflex">
    <h2>FUSSREFLEX-MASSAGE</h2>
    <p>Das Prinzip beruht auf der Erkenntnis, dass Energiezonen durch den Körper laufen. In den Füssen reflektieren sich diese Zonen und korrespondieren mit den wichtigen Organen, Drüsen und anderen Körperteilen. Durch Druck von Finger und Daumen am Fuss beeinflusst das die entsprechende Zone im ganzen Körper. Es werden über <strong>1'000 Nervenenden während einer Fussreflexzonenmassage stimuliert.</strong></p>
  </div>
  <div class="section section--quantum">
    <h2>QUANTENHEILUNG</h2>
    <p>Transformationen-Methoden die eine positive Veränderung über das höhere Bewusstsein auf unseren allgemein Zustand herbeiführt z.B.</p>
    <ul>
      <li>Glaubenssätze und Blockaden lösen</li>
      <li>Burnout</li>
      <li>Partnerschaft Probleme</li>
      <li>Geldmangel und Fehlendes Einkommen</li>
      <li>Berufliche o. Private Veränderung</li>
      <li>Gesundheitliche Beschwerden</li>
      <li>Übergewicht</li>
      <li>Zielfindung und Erreichung</li>
      <li>Depressionen / Sexualität / Missbrauch</li>
    </ul>
  </div>
  <div class="frame" style="left:17px;top:16px;width:453px;height:657px"></div>
</section>

</body>
</html>
```